Marolina Swimming & Athletics Center

We need Business Card for a Athletics center
The logo frome the Uploaded Files ( b card fimal)
Οn one side of card we need the logo of company the Contact and the website:
1. Address:(Limassol, Cyprus 12-14 Dravelonos str,Ano Feralia,P.C. 5280)

2.Phone number: (+357) 25-804273

3. Mail: info@marolinasport.example

3. Website: www.marolinasport.example

Οn the other side of the card we need to write the sport of the company:

1. Artistic Gymnastics
2. Swimming
3. Gym - Fitness
4. Programs
5. Dancing
5.Tennis

From the Uploaded Files you can get the logo.In a logo is behind the black color which can be removed from logo.

Υou can use that color you want.
.

Industry/Entity Type

Business

Font styles to use
Decorative

Colors
0555a3
ffcf3e
3176b5
0692cd
add136
f04a50
000000
cfcfcf
9d9d9d

Requirements
Should not have
• photos with faces
• photo fro the Website:www.marolinasport.example

```html
<!DOCTYPE html>
<html lang="en">
<head>
<meta charset="utf-8">
<title>Marolina Swimming &amp; Athletics Center – Business Card</title>
<link rel="stylesheet" href="https://fonts.googleapis.com/css2?family=Roboto+Condensed:wght@400;700&display=swap">
<style>
  :root {
    --backdrop: #e9e6e1;
    --card-black: #0d0d0d;
    --gold: #ffcf3e;
    --gold-deep: #d99a1c;
    --gold-light: #ffe9a0;
    --white: #ffffff;
    --silver: #cfcfcf;
    --grey: #9d9d9d;
    --aqua: #5fcde0;
    --blue: #0555a3;
  }
  * { box-sizing: border-box; margin: 0; padding: 0; }
  html, body { width: 1200px; height: 780px; overflow: hidden; }
  body {
    background: var(--backdrop);
    font-family: "Roboto Condensed", "Arial Narrow", sans-serif;
    display: flex;
    align-items: center;
    justify-content: center;
    gap: 28px;
  }
  .card {
    width: 556px;
    height: 318px;
    background: var(--card-black);
    box-shadow: 0 10px 26px rgba(0,0,0,.28);
    position: relative;
    overflow: hidden;
  }

  /* Front side */
  .front { display: flex; flex-direction: column; }
  .front-header {
    height: 118px;
    display: flex;
    align-items: center;
    padding: 0 26px;
    gap: 16px;
  }
  .wordmark {
    font-weight: 700;
    color: var(--gold);
    letter-spacing: 2px;
    text-transform: uppercase;
    line-height: 1;
  }
  .front-header .wordmark { font-size: 44px; }
  .brand-dot {
    width: 46px; height: 46px;
    border-radius: 50%;
    background: var(--gold);
    flex: none;
  }
  .center-name {
    margin-left: auto;
    color: var(--white);
    font-weight: 700;
    font-size: 19px;
    line-height: 1.1;
    text-transform: uppercase;
    text-align: right;
    letter-spacing: .5px;
  }
  .gold-rule {
    height: 5px;
    background: linear-gradient(90deg, var(--gold-deep), var(--gold), var(--gold-deep));
    border-bottom: 3px solid var(--white);
  }
  .photo-strip {
    flex: 1;
    display: flex;
    gap: 3px;
    background: var(--white);
  }
  .photo { flex: 1; }
  .photo.fitness-model { background: linear-gradient(160deg, #f4f4f4, #d9d3cc); }
  .photo.weight-training { background: linear-gradient(160deg, #eeeeee, #c9b8a8); }
  .photo.pommel-horse { background: linear-gradient(180deg, #121212, #1f3c7a); }
  .photo.swimmer { background: linear-gradient(160deg, #8fe3f0, var(--aqua)); }
  .photo.dancers { background: linear-gradient(160deg, #8a8a8a, #3a3a3a); }
  .sports-band {
    height: 46px;
    border-top: 3px solid var(--white);
    background: linear-gradient(180deg, var(--gold-light), var(--gold) 45%, var(--gold-deep));
    display: flex;
    align-items: center;
    justify-content: center;
    color: #1a1a1a;
    font-size: 14.5px;
    font-weight: 400;
    letter-spacing: .4px;
    text-transform: uppercase;
    white-space: nowrap;
  }

  /* Back side */
  .back {
    display: flex;
    flex-direction: column;
    align-items: center;
    justify-content: center;
    text-align: center;
  }
  .back .wordmark { font-size: 64px; letter-spacing: 3px; margin-bottom: 18px; }
  .person-name {
    color: var(--gold);
    font-weight: 700;
    font-size: 17px;
    text-transform: uppercase;
  }
  .person-role {
    color: var(--silver);
    font-size: 13px;
    margin-bottom: 14px;
  }
  .contact-line {
    color: var(--white);
    font-size: 15px;
    line-height: 1.5;
  }
  .website {
    color: var(--gold);
    font-size: 15px;
    font-weight: 700;
    margin-top: 6px;
  }
</style>
</head>
<body>
  <section class="card front" aria-label="Card front">
    <header class="front-header">
      <span class="wordmark">Marolina</span>
      <span class="brand-dot"></span>
      <h1 class="center-name">Marolina Swimming<br>&amp; Athletics Center</h1>
    </header>
    <div class="gold-rule"></div>
    <div class="photo-strip">
      <div class="photo fitness-model" role="img" aria-label="Photo of an athlete lifting a dumbbell"></div>
      <div class="photo weight-training" role="img" aria-label="Photo of arm weight training"></div>
      <div class="photo pommel-horse" role="img" aria-label="Photo of a gymnast on a pommel horse"></div>
      <div class="photo swimmer" role="img" aria-label="Photo of a swimmer in a pool"></div>
      <div class="photo dancers" role="img" aria-label="Black and white photo of leaping dancers"></div>
    </div>
    <p class="sports-band">Artistic Gymnastics | Swimming | Gym - Fitness | Programs | Dancing | Tennis</p>
  </section>

  <section class="card back" aria-label="Card back">
    <span class="wordmark">Marolina</span>
    <p class="person-name">Dara Kostel</p>
    <p class="person-role">Owner</p>
    <p class="contact-line">(+357) 25-804273</p>
    <p class="contact-line">info@marolinasport.example</p>
    <p class="contact-line">Limassol, Cyprus 12-14 Dravelonos str,Ano Feralia,P.C. 5280</p>
    <p class="website">www.marolinasport.example</p>
  </section>
</body>
</html>
```